Salon and Spa Distributor Business Card

Need a business card. We are are distributor in the salon and spa industry. We identify with natural beauty. Need a card with:
Company Name: Petal Haven"
Title: "President & CEO"
Address
Company Phone number
email
website
Tag Line:" The Professional Salon Source"

Industry/Entity Type

Business

Contact Information for Business Card

Name: Lena Morcott
Title: "President & CEO"
Address: 317 Birchfield Ln, Oakvane, NJ 07481
Company Phone number: 800-463-9152
email: lenamorcott@petalhaven-example.com
website: www.petalhaven-example.com

Requirements
Should not have
• No black backgrounds

```html
<!DOCTYPE html>
<html lang="en">
<head>
<meta charset="utf-8">
<title>Petal Haven Business Card</title>
<link rel="stylesheet" href="https://fonts.googleapis.com/css2?family=Montserrat:wght@700&family=Questrial&display=swap">
<style>
  :root {
    --backdrop: #d6d6d6;
    --card: #ffffff;
    --brand-green: #3aa84a;
    --deep-green: #00a651;
    --leaf-green: #8cc63f;
    --teal: #10b1c8;
    --teal-light: #4cc6d2;
    --ink: #1a1a1a;
    --muted: #6b6b6b;
    --rule: #9a9a9a;
  }
  html, body {
    margin: 0;
    width: 1200px;
    height: 800px;
    overflow: hidden;
    background: var(--backdrop);
  }
  .stage {
    position: relative;
    width: 1200px;
    height: 800px;
  }
  .card {
    position: absolute;
    top: 272px;
    width: 472px;
    height: 263px;
    background: var(--card);
    overflow: hidden;
  }
  .card--front { left: 60px; }
  .card--back { left: 641px; }

  .brand-dot {
    flex: none;
    border-radius: 50%;
    background: var(--leaf-green);
  }
  .brand-name {
    font-family: "Questrial", sans-serif;
    color: var(--brand-green);
    white-space: nowrap;
    line-height: 1;
  }

  /* Front */
  .front-brand {
    position: absolute;
    left: 120px;
    top: 76px;
    display: flex;
    align-items: center;
    gap: 17px;
  }
  .front-brand .brand-dot { width: 56px; height: 56px; }
  .front-brand .brand-name { font-size: 31px; display: block; }
  .tagline {
    display: block;
    margin-top: 7px;
    font-family: "Questrial", sans-serif;
    font-size: 11px;
    letter-spacing: 0.8px;
    color: var(--muted);
    white-space: nowrap;
  }
  .front-waves {
    position: absolute;
    left: 0;
    bottom: 0;
    width: 472px;
    height: 80px;
  }

  /* Back */
  .back-brand {
    position: absolute;
    left: 64px;
    top: 33px;
    display: flex;
    align-items: center;
    gap: 25px;
  }
  .back-brand .brand-dot { width: 30px; height: 30px; }
  .back-brand .brand-name { font-size: 14px; }
  .holder {
    position: absolute;
    left: 252px;
    top: 37px;
  }
  .holder-name {
    font-family: "Montserrat", sans-serif;
    font-weight: 700;
    font-size: 19px;
    letter-spacing: 0.5px;
    color: var(--ink);
    margin: 0;
    line-height: 1;
  }
  .holder-name .surname { color: var(--deep-green); margin-left: 6px; }
  .holder-title {
    font-family: "Questrial", sans-serif;
    font-size: 9.5px;
    letter-spacing: 1px;
    color: var(--muted);
    margin: 6px 0 0;
  }
  .divider {
    position: absolute;
    left: 31px;
    top: 97px;
    width: 409px;
    height: 1px;
    background: var(--rule);
  }
  .contacts {
    position: absolute;
    left: 254px;
    top: 124px;
    margin: 0;
    padding: 0;
    list-style: none;
    font-family: "Questrial", sans-serif;
    font-size: 10px;
    color: var(--ink);
  }
  .contacts li {
    display: flex;
    align-items: flex-start;
    gap: 6px;
    margin-bottom: 4px;
    line-height: 12px;
  }
  .contacts svg { flex: none; width: 11px; height: 11px; margin-top: 1px; }
  .color-bands {
    position: absolute;
    left: 0;
    bottom: 0;
    width: 472px;
    height: 24px;
    display: flex;
  }
  .band { height: 100%; }
  .band--teal { width: 155px; background: var(--teal-light); }
  .band--leaf { width: 159px; background: var(--leaf-green); }
  .band--green { flex: 1; background: var(--deep-green); }
</style>
</head>
<body>
<main class="stage">
  <section class="card card--front">
    <div class="front-brand">
      <span class="brand-dot"></span>
      <div class="brand-text">
        <span class="brand-name">Petal Haven</span>
        <span class="tagline">The Professional Salon Source</span>
      </div>
    </div>
    <svg class="front-waves" viewBox="0 0 472 80" preserveAspectRatio="none" aria-hidden="true">
      <path d="M110 80 C220 40 340 4 472 0 L472 80 Z" fill="var(--teal)"/>
      <path d="M0 36 C60 32 120 36 200 50 C300 66 400 70 472 62 L472 80 L0 80 Z" fill="var(--leaf-green)"/>
      <path d="M0 62 C110 38 220 26 320 34 C400 42 440 52 472 58 L472 80 L0 80 Z" fill="var(--deep-green)" opacity="0.92"/>
    </svg>
  </section>

  <section class="card card--back">
    <div class="back-brand">
      <span class="brand-dot"></span>
      <span class="brand-name">Petal Haven</span>
    </div>
    <div class="holder">
      <h1 class="holder-name">LENA<span class="surname">MORCOTT</span></h1>
      <p class="holder-title">PRESIDENT &amp; CEO</p>
    </div>
    <div class="divider"></div>
    <ul class="contacts">
      <li>
        <svg viewBox="0 0 12 12" aria-hidden="true"><path d="M1 6 L6 1.5 L11 6 V11 H1 Z" fill="var(--deep-green)"/><rect x="4.5" y="7" width="3" height="4" fill="#fff"/></svg>
        <span>317 Birchfield Ln, Oakvane,<br>NJ 07481</span>
      </li>
      <li>
        <svg viewBox="0 0 12 12" aria-hidden="true"><rect x="3" y="0.5" width="6" height="11" rx="1" fill="var(--deep-green)"/><rect x="4.2" y="2" width="3.6" height="5.5" fill="#fff"/></svg>
        <span>800-463-9152</span>
      </li>
      <li>
        <svg viewBox="0 0 12 12" aria-hidden="true"><rect x="0.5" y="2" width="11" height="8" fill="var(--deep-green)"/><path d="M0.5 2 L6 6.5 L11.5 2" stroke="#fff" fill="none"/></svg>
        <span>lenamorcott@petalhaven-example.com</span>
      </li>
      <li>
        <svg viewBox="0 0 12 12" aria-hidden="true"><rect x="1" y="5" width="6" height="3.2" rx="1.6" transform="rotate(-45 4 6.6)" stroke="var(--deep-green)" stroke-width="1.4" fill="none"/><rect x="5" y="3.8" width="6" height="3.2" rx="1.6" transform="rotate(-45 8 5.4)" stroke="var(--deep-green)" stroke-width="1.4" fill="none"/></svg>
        <span>www.petalhaven-example.com</span>
      </li>
    </ul>
    <div class="color-bands">
      <span class="band band--teal"></span>
      <span class="band band--leaf"></span>
      <span class="band band--green"></span>
    </div>
  </section>
</main>
</body>
</html>
```